Updated brief for New ecommerce site needs a stunning business card that links to web site.

Updated business card brief. Please refer to the new files uploaded today (the last two) which show the background colour/style that we will be using in our web template for on-line trading, the grey marble concrete look.

Please see if you can use the grey marble background in the business card design in a way so it relates to our web template. It also needs to be transferable to banner ad, chatterbay ad etc.
quarnel hub is a NEW eCommerce website which is commencing selling via tradlo & sellnook, used & damaged mobile phones & accessories, evolving into a full eCommerce store.

We like strong clean lines, use of a circle, in essence this will become our logo as well. Colours strong orange/Black/White The orange stronger than in CraftPanel #5352704 & grey marble as per file attached #153082

We love the use of a circle!! As we are evolving & moving forward this is what the circle represents to us……. ongoing change.

Front side with a circle with quarnel hub in a modern font in the middle, brivo is in a strong orange and group is in black or white. On the reverse side, use layout as per Lumerax design from pelk.example. for icon details (not the boarder at top/botto).

This design is to meet www.pelk.example luxe cards specifications
Thank you we look forward to last minute inspiration.
Updates

Target Market(s)

Suppliers & business networking

Industry/Entity Type

Business

Contact Information for Business Card

Sam Ruiz
Director
mob +61 4987 6543
Locked Bag WXYZ 5678 QRS
sam@quarnelhub.example.au
www.quarnelhub.example.au

Requirements
Must have
• Design to meet www.pelk.example luxe business card specifications
• Colours - orange needs to be bold and strong & /black/white
• Circle with quarnel hub in the middle
Nice to have
• Grey marble background incorporated into design in someway so it links with our web page.

```html
<!DOCTYPE html>
<html lang="en">
<head>
<meta charset="utf-8">
<title>quarnel hub business card</title>
<link rel="stylesheet" href="https://fonts.googleapis.com/css2?family=Arimo:wght@400;700&display=swap">
<style>
  :root {
    --orange: #e25f15;
    --black: #060707;
    --white: #ffffff;
    --stage: #c9c9c9;
    --rule: #8a8a8a;
  }
  * { margin: 0; padding: 0; box-sizing: border-box; }
  html, body { width: 1200px; height: 1000px; overflow: hidden; }
  body {
    position: relative;
    background: var(--stage);
    font-family: "Arimo", Arial, sans-serif;
    color: var(--white);
  }
  .card {
    position: absolute;
    left: 352px;
    width: 518px;
    height: 339px;
  }
  .card-front { top: 146px; background: var(--orange); }
  .card-back { top: 544px; background: var(--black); }

  .brand {
    position: absolute;
    left: 0; right: 0; top: 148px;
    display: flex; align-items: center; justify-content: center;
    gap: 14px;
  }
  .brand-dot {
    width: 22px; height: 22px;
    border-radius: 50%;
    background: var(--black);
    flex: none;
  }
  .brand-name {
    font-weight: 700;
    font-size: 36px;
    line-height: 42px;
    color: var(--black);
  }
  .web-address {
    position: absolute;
    left: 0; right: 0; top: 293px;
    text-align: center;
    font-weight: 700;
    font-size: 18px;
  }

  .holder { position: absolute; left: 110px; top: 120px; }
  .holder-name { font-weight: 700; font-size: 24px; color: var(--orange); line-height: 28px; }
  .holder-role { font-size: 20px; line-height: 24px; }
  .divider {
    position: absolute; left: 38px; top: 184px;
    width: 442px; height: 2px;
    background: linear-gradient(to right, transparent, var(--rule) 20%, var(--rule) 80%, transparent);
  }
  .contact-list { position: absolute; left: 78px; top: 206px; list-style: none; }
  .contact-item {
    display: flex; align-items: center;
    height: 28.5px;
    font-weight: 700; font-size: 21px;
  }
  .contact-icon { width: 20px; height: 20px; margin-right: 13px; flex: none; }
  .contact-icon * { fill: none; stroke: var(--orange); stroke-width: 2; stroke-linecap: round; stroke-linejoin: round; }
  .contact-icon .solid { fill: var(--orange); stroke: none; }
</style>
</head>
<body>
  <section class="card card-front">
    <div class="brand">
      <span class="brand-dot"></span>
      <span class="brand-name">quarnel hub</span>
    </div>
    <p class="web-address">www.quarnelhub.example.au</p>
  </section>

  <section class="card card-back">
    <div class="holder">
      <p class="holder-name">Sam Ruiz</p>
      <p class="holder-role">Director</p>
    </div>
    <div class="divider"></div>
    <ul class="contact-list">
      <li class="contact-item">
        <svg class="contact-icon" viewBox="0 0 20 20"><path class="solid" d="M5 2 L8 2 L9 6 L7 8 Q9 12 12 14 L14 12 L18 13 L18 16 Q17 19 14 18 Q5 15 2 6 Q2 3 5 2 Z"/></svg>
        +61 7 5550 8642
      </li>
      <li class="contact-item">
        <svg class="contact-icon" viewBox="0 0 20 20"><rect x="6" y="2" width="9" height="16" rx="1.5"/><line x1="10.5" y1="15" x2="10.5" y2="15.2"/></svg>
        +61 4987 6543
      </li>
      <li class="contact-item">
        <svg class="contact-icon" viewBox="0 0 20 20"><path d="M10 18 L7 13.5 A6 6 0 1 1 13 13.5 Z"/></svg>
        Locked Bag WXYZ 5678 QRS
      </li>
      <li class="contact-item">
        <svg class="contact-icon" viewBox="0 0 20 20"><rect x="2" y="5" width="16" height="11"/><path d="M2 5 L10 12 L18 5"/></svg>
        sam@quarnelhub.example.au
      </li>
    </ul>
  </section>
</body>
</html>
```